Harborline Stay Collective Business Card Design

Design a business card for Harborline Stay Collective. Look at the website for colors and reference. Card should have logo, name, title, office number, mobile number, email, URL and a tagline like, "Luxury Hotel & Resort Email Marketing" (This might change).

https://www.harborlinestaycollective.net

The rest I will leave up to your imagination.

Contact Information for Business Card

Logo, name, title, office number, mobile number, email, URL and a tagline like, "Luxury Hotel & Resort Email Marketing" (This might change).

```html
<!DOCTYPE html>
<html lang="en">
<head>
<meta charset="utf-8">
<title>Harborline Stay Collective – Business Card</title>
<link rel="stylesheet" href="https://fonts.googleapis.com/css2?family=Arimo:wght@400;700&display=swap">
<style>
  :root {
    --orange: #f57c14;
    --orange-light: #f99236;
    --ink: #1c1c1c;
    --grey-text: #6f6f6f;
    --paper: #ffffff;
    --backdrop: #b9b8b8;
  }
  * { margin: 0; padding: 0; box-sizing: border-box; }
  html, body { width: 1200px; height: 876px; overflow: hidden; }
  body {
    background: radial-gradient(ellipse at 45% 30%, #cfcece 0%, var(--backdrop) 70%);
    font-family: "Arimo", Arial, sans-serif;
    position: relative;
  }
  .card {
    position: absolute;
    width: 540px;
    height: 310px;
    box-shadow: 0 6px 18px rgba(0,0,0,.22);
    overflow: hidden;
  }
  /* back side */
  .card-back {
    left: 610px; top: 130px;
    background: linear-gradient(135deg, var(--orange-light) 0%, var(--orange) 60%);
    display: flex; align-items: center; justify-content: center;
  }
  .card-back .brand-name { font-size: 30px; }
  /* front side */
  .card-front {
    left: 50px; top: 436px;
    background: var(--paper);
  }
  .front-wave { position: absolute; inset: 0; }
  .brand-name {
    font-family: "Arimo", Arial, sans-serif;
    font-weight: 700;
    color: var(--ink);
    text-transform: uppercase;
    letter-spacing: 1px;
    line-height: 1.05;
    text-align: center;
  }
  .card-front .brand-name {
    position: absolute; left: 70px; top: 62px; width: 215px;
    font-size: 19px;
  }
  .contact {
    position: absolute; left: 300px; top: 48px;
    padding-left: 16px;
    border-left: 1px solid var(--orange);
    color: var(--grey-text);
    font-size: 13px;
    line-height: 1.45;
  }
  .contact .person-name {
    color: var(--orange); font-weight: 700; font-size: 17px; letter-spacing: .5px;
    text-transform: uppercase; line-height: 1.1;
  }
  .contact .person-title { font-size: 13px; margin-bottom: 10px; }
  .contact .address { margin-bottom: 8px; }
  .contact-row { display: flex; align-items: center; gap: 7px; }
  .contact-row svg { width: 11px; height: 11px; flex: none; }
</style>
</head>
<body>

<section class="card card-back" aria-label="Card back">
  <p class="brand-name">Harborline Stay<br>Collective</p>
</section>

<section class="card card-front" aria-label="Card front">
  <svg class="front-wave" viewBox="0 0 540 310" aria-hidden="true">
    <path d="M0 78 C28 82 44 150 88 218 C128 278 300 298 540 304 L540 310 L0 310 Z" fill="var(--orange)"/>
    <path d="M0 68 C30 72 48 142 94 210 C136 270 300 290 540 297" fill="none" stroke="var(--ink)" stroke-width="5"/>
  </svg>

  <p class="brand-name">Harborline Stay<br>Collective</p>

  <div class="contact">
    <p class="person-name">Daniel Harper</p>
    <p class="person-title">Manager</p>
    <p class="address">Your Address, City<br>State, Zip 0000</p>
    <p class="contact-row">
      <svg viewBox="0 0 12 12"><path d="M2 1 L4 1 L5 4 L3.6 5 C4.3 6.6 5.4 7.7 7 8.4 L8 7 L11 8 L11 10 C11 10.6 10.6 11 10 11 C5 11 1 7 1 2 C1 1.4 1.4 1 2 1 Z" fill="var(--orange)"/></svg>
      123-456-2100
    </p>
    <p class="contact-row">
      <svg viewBox="0 0 12 12"><rect x="3" y="0.8" width="6" height="10.4" rx="1" fill="none" stroke="var(--orange)" stroke-width="1.2"/><circle cx="6" cy="9.4" r=".7" fill="var(--orange)"/></svg>
      123-456-2100
    </p>
    <p class="contact-row">
      <svg viewBox="0 0 12 12"><rect x="0.8" y="2.5" width="10.4" height="7" fill="none" stroke="var(--orange)" stroke-width="1.2"/><path d="M1 3 L6 7 L11 3" fill="none" stroke="var(--orange)" stroke-width="1.2"/></svg>
      youremail@mailbox.com
    </p>
    <p class="contact-row">
      <svg viewBox="0 0 12 12"><circle cx="6" cy="6" r="5.2" fill="var(--orange)"/><path d="M1 6 H11 M6 1 C3.5 3.5 3.5 8.5 6 11 M6 1 C8.5 3.5 8.5 8.5 6 11" fill="none" stroke="#fff" stroke-width=".8"/></svg>
      www.yourwebsite.com
    </p>
  </div>
</section>

</body>
</html>
```